Poster design for a company operating care homes in the UK showcasing our core values

We need a poster to display in our care homes showcasing our new core values:

Purpose
We are driven by a clear understanding of why we do what we do: to enrich lives, honour legacies and make a meaningful difference every day, for our residents, their families, our colleagues and our community.

Excellence
We hold ourselves to the highest standards, delivering exceptional care and creating an environment where both residents and staff can thrive.

Openness
We build trust through honest, respectful communication, welcoming feedback, sharing ideas, and embracing change as a path to continuous growth.

Passion
We are passionate about delivering exceptional care. We take pride in what we do and in making a real difference in people’s lives.

Learning
We are committed to personal and professional growth; empowering each other through ongoing development, reflection, and shared knowledge.

Empathy
We actively listen and seek to understand before being understood, recognising the unique stories, feelings, and needs of others.

I have attached a small graphic that we would like you try to incorporate, in addition to our company logo. Please theme the rest of the poster around our company colours.

```html
<!DOCTYPE html>
<html lang="en">
<head>
<meta charset="utf-8">
<title>Corvale – Core Values</title>
<link href="https://fonts.googleapis.com/css2?family=Poppins:wght@400;500;600;700&display=swap" rel="stylesheet">
<style>
  :root {
    --paper: #f6e6df;
    --navy: #3a5272;
    --peach: #e6a27f;
    --white: #ffffff;
  }
  * { margin: 0; padding: 0; box-sizing: border-box; }
  html, body { width: 848px; height: 1200px; overflow: hidden; background: var(--paper); }
  .poster {
    position: relative;
    width: 848px;
    height: 1200px;
    background: var(--paper);
    font-family: "Poppins", sans-serif;
    color: var(--navy);
    overflow: hidden;
  }
  .header-swoosh { position: absolute; top: 0; left: 0; width: 848px; height: 260px; }
  .brand {
    position: absolute;
    top: 26px;
    left: 540px;
    display: flex;
    align-items: center;
    gap: 12px;
    font-weight: 700;
    font-size: 34px;
    letter-spacing: 2px;
    color: var(--navy);
  }
  .brand-square { width: 26px; height: 26px; background: var(--peach); }
  .values { position: absolute; left: 0; top: 0; width: 100%; }
  .value { position: absolute; left: 38px; }
  .value-title {
    display: flex;
    align-items: center;
    gap: 19px;
    font-weight: 600;
    font-size: 31px;
    letter-spacing: 2.6px;
    line-height: 40px;
  }
  .value-title::before {
    content: "";
    width: 11px;
    height: 11px;
    border-radius: 50%;
    background: var(--peach);
    flex: none;
  }
  .value-text {
    margin-left: 29px;
    margin-top: 8px;
    font-size: 18.4px;
    line-height: 22.5px;
    font-weight: 400;
  }
  .values-graphic {
    position: absolute;
    left: 250px;
    top: 1033px;
    width: 362px;
    height: 94px;
    border-radius: 14px;
    background: linear-gradient(90deg, var(--peach), var(--navy));
  }
  .footer-bands { position: absolute; left: 0; bottom: 0; width: 100%; height: 26px; }
  .band { position: absolute; left: 0; width: 100%; }
  .band-top { top: 0; height: 6px; background: var(--navy); }
  .band-mid { top: 10px; height: 5px; background: var(--peach); }
  .band-base { top: 19px; height: 7px; background: var(--navy); }
</style>
</head>
<body>
<main class="poster">
  <svg class="header-swoosh" viewBox="0 0 848 260" aria-hidden="true">
    <path d="M400 0 C470 80 600 115 848 95 L848 252 C740 200 560 205 400 0 Z" fill="var(--navy)"/>
    <text x="700" y="172" text-anchor="middle" transform="rotate(12 700 172)"
          font-family="Poppins, sans-serif" font-weight="600" font-size="27" letter-spacing="3"
          fill="var(--peach)">CORE VALUES</text>
  </svg>

  <div class="brand"><span class="brand-square"></span>CORVALE</div>

  <section class="values">
    <article class="value" style="top:136px">
      <h2 class="value-title">PURPOSE</h2>
      <p class="value-text">We are driven by a clear understanding<br>of why we do what we do: to enrich lives, honour<br>legacies and make a meaningful difference every day,<br>for our residents, their families,our colleagues and our community.</p>
    </article>
    <article class="value" style="top:306px">
      <h2 class="value-title">EXCELLENCE</h2>
      <p class="value-text">We hold ourselves to the highest standards, delivering exceptional<br>care and creating an environment where both residents and<br>staff can thrive.</p>
    </article>
    <article class="value" style="top:454px">
      <h2 class="value-title">OPENNESS</h2>
      <p class="value-text">We build trust through honest, respectful communication, welcoming<br>feedback, sharing ideas, and embracing change as a path to<br>continuous growth.</p>
    </article>
    <article class="value" style="top:601px">
      <h2 class="value-title">PASSION</h2>
      <p class="value-text">We are passionate about delivering exceptional care. We take pride<br>in what we do and in making a real difference in people’s lives.</p>
    </article>
    <article class="value" style="top:723px">
      <h2 class="value-title">LEARNING</h2>
      <p class="value-text">We are committed to personal and professional growth; empowering<br>each other through ongoing development, reflection, and<br>shared knowledge.</p>
    </article>
    <article class="value" style="top:871px">
      <h2 class="value-title">EMPATHY</h2>
      <p class="value-text">We actively listen and seek to understand before being understood,<br>recognising the unique stories, feelings, and needs of others.</p>
    </article>
  </section>

  <div class="values-graphic" role="img" aria-label="PEOPLE values graphic: a row of hexagons spelling the six core values"></div>

  <div class="footer-bands" aria-hidden="true">
    <span class="band band-top"></span>
    <span class="band band-mid"></span>
    <span class="band band-base"></span>
  </div>
</main>
</body>
</html>
```